Label design needed for cafe display

Hi,
We need a label designed so that we can label food in our display fridge.
The label would have to be editable, as we have lot's of different food items.. and we change the items often, so I would be constantly updating the labels. I will then be printing each label, and laminating them, then displaying them in our food display fridge.
We would like the label to contain our logo - which I have attached.
I have also attached our menus, so you can get a feel for the designs we like.
An example of what we need on a label:
QUICHE LORRAINE $7.50
With Salad $9.50
Please feel free to ask me any questions.
Printing

```html
<!DOCTYPE html>
<html lang="en">
<head>
<meta charset="utf-8">
<title>Good Measure – Display Fridge Labels</title>
<link rel="stylesheet" href="https://fonts.googleapis.com/css2?family=Cinzel:wght@700&family=Josefin+Sans:ital,wght@1,400&family=Open+Sans:wght@600&display=swap">
<style>
  :root {
    --brown: #3f2d2c;
    --cream: #fbf5a9;
    --white: #ffffff;
    --ink: #111111;
  }
  * { box-sizing: border-box; margin: 0; padding: 0; }
  html, body { width: 873px; height: 1200px; overflow: hidden; background: var(--white); }
  .sheet { position: relative; width: 873px; height: 1200px; }
  .abs { position: absolute; }

  /* brand name: plain text with one small circle beside it */
  .brand {
    position: absolute;
    display: flex; align-items: center; justify-content: center; gap: 0.4em;
    font-family: "Open Sans", sans-serif;
    font-weight: 600;
    color: var(--brown);
    white-space: nowrap;
    line-height: 1;
  }
  .brand::before {
    content: ""; width: 0.6em; height: 0.6em; border-radius: 50%;
    background: var(--brown); flex: none;
  }

  .ribbon { position: absolute; }
  .ribbon svg { position: absolute; inset: 0; width: 100%; height: 100%; }
  .ribbon .price {
    position: relative; height: 100%;
    display: flex; flex-direction: column; align-items: center; justify-content: center;
    text-align: center;
  }

  .price-italic {
    font-family: "Josefin Sans", sans-serif;
    font-style: italic;
    color: var(--white);
    font-size: 22px;
    letter-spacing: 4px;
    line-height: 1.45;
    text-align: center;
  }
  .price-serif {
    font-family: "Cinzel", serif;
    font-weight: 700;
    color: var(--brown);
    font-size: 18px;
    line-height: 1.15;
    letter-spacing: -0.3px;
  }
  .price-sans {
    font-family: "Open Sans", sans-serif;
    font-weight: 600;
    color: var(--white);
    font-size: 23px;
    line-height: 1.3;
    text-align: center;
  }

  /* label 1: oval */
  .label-oval {
    left: 8px; top: 5px; width: 539px; height: 375px;
    border-radius: 50%; background: var(--brown);
  }
  .label-oval .inner-line {
    position: absolute; inset: 10px; border-radius: 50%;
    border: 2px solid var(--white);
  }
  .label-oval .brand-tile {
    position: absolute; left: 198px; top: 37px; width: 170px; height: 117px;
    background: var(--cream);
  }

  /* label 2: dark card with cream oval */
  .label-card-dark {
    left: 550px; top: 228px; width: 309px; height: 354px; background: var(--brown);
  }
  .label-card-dark .cream-oval {
    position: absolute; left: 20px; top: 23px; width: 269px; height: 319px;
    border-radius: 50%; background: var(--cream);
  }

  /* label 3: cream box with bar */
  .label-box {
    left: 22px; top: 382px; width: 468px; height: 379px;
    background: var(--cream); border: 3px solid var(--ink);
  }
  .price-bar {
    position: absolute; background: var(--brown);
    display: flex; flex-direction: column; align-items: center; justify-content: center;
  }
  .price-bar::after {
    content: ""; position: absolute; inset: 6px; border: 3px solid var(--white);
    pointer-events: none;
  }

  /* label 4: tent label */
  .label-tent-top {
    left: 119px; top: 792px; width: 305px; height: 222px;
    background: var(--cream); border: 5px solid var(--ink); border-bottom: none;
  }

  /* label 5: tall tag */
  .label-tag {
    left: 559px; top: 598px; width: 286px; height: 588px;
    background: var(--cream); border: 3px solid var(--ink); border-radius: 16px;
  }
  .label-tag .price-oval {
    position: absolute; left: 11px; top: 228px; width: 259px; height: 348px;
    border-radius: 50%; background: var(--brown);
    display: flex; align-items: center; justify-content: center;
  }
  .label-tag .price-oval::after {
    content: ""; position: absolute; inset: 9px; border-radius: 50%;
    border: 4px solid var(--white);
  }
  .label-tag .price-sans { font-size: 26px; line-height: 1.35; position: relative; }
</style>
</head>
<body>
<main class="sheet">

  <!-- Oval label -->
  <section class="abs label-oval">
    <div class="inner-line"></div>
    <div class="brand-tile">
      <div class="brand" style="inset:0; font-size:19px;">Good Measure</div>
    </div>
    <div class="ribbon" style="left:49px; top:186px; width:443px; height:82px;">
      <svg viewBox="0 0 443 82" preserveAspectRatio="none" aria-hidden="true">
        <polygon points="2,2 441,2 416,41 441,80 2,80 27,41" fill="none" stroke="#ffffff" stroke-width="3"/>
      </svg>
      <div class="price price-italic">
        <span>QUICHE LORRAINE $7.50</span>
        <span>With Salad $9.50</span>
      </div>
    </div>
  </section>

  <!-- Dark card label -->
  <section class="abs label-card-dark">
    <div class="cream-oval"></div>
    <div class="brand" style="left:20px; width:269px; top:100px; font-size:22px;">Good Measure</div>
    <div class="ribbon" style="left:4px; top:185px; width:301px; height:75px;">
      <svg viewBox="0 0 301 75" preserveAspectRatio="none" aria-hidden="true">
        <polygon points="2,2 299,2 277,37.5 299,73 2,73 24,37.5" fill="#ffffff" stroke="#3f2d2c" stroke-width="3"/>
      </svg>
      <div class="price price-serif">
        <span>QUICHE LORRAINE $7.50</span>
        <span>WITH SALAD $9.50</span>
      </div>
    </div>
  </section>

  <!-- Cream box label -->
  <section class="abs label-box">
    <div class="brand" style="left:0; width:462px; top:100px; font-size:36px;">Good Measure</div>
    <div class="price-bar" style="left:13px; top:231px; width:436px; height:131px;">
      <div class="price-italic">
        <div>QUICHE LORRAINE $7.50</div>
        <div>With Salad $9.50</div>
      </div>
    </div>
  </section>

  <!-- Tent label -->
  <section class="abs label-tent-top">
    <div class="brand" style="left:0; width:295px; top:95px; font-size:28px;">Good Measure</div>
  </section>
  <div class="price-bar" style="left:63px; top:1009px; width:414px; height:146px; border:3px solid var(--ink);">
    <div class="price-sans">
      <div>QUICHE LORRAINE $7.50</div>
      <div>With Salad $9.50</div>
    </div>
  </div>

  <!-- Tall tag label -->
  <section class="abs label-tag">
    <div class="brand" style="left:0; width:280px; top:100px; font-size:28px;">Good Measure</div>
    <div class="price-oval">
      <div class="price-sans">
        <div>QUICHE</div>
        <div>LORRAINE</div>
        <div>$7.50</div>
        <div>With Salad</div>
        <div>$9.50</div>
      </div>
    </div>
  </section>

</main>
</body>
</html>
```